Veteran Owned General Contractor needs Bold New Business Cards

We are a service disabled veteran owned small business. We're a general contractor that specializes in excavation, underground utilities, site work, land clearing and demolition. We would like a fresh, simple, bold, new look for our business cards. We're open to ideas! We'd like to incorporate the following information on the card:

Company Name & Logo, Name of Person, Job Title, Office Phone, Fax, Cell Phone, Email Address, Website, SDVOSB

Our logo is included. We look forward to your thoughts.

Thank you!
Updates

Reason: Hello Due to the overwhelming response to this project, we are extending the deadline one time to allow for improved communication and feedback with the top candidates. We would like to thank everyone for their hard work and exceptional creativity! Thank you

Industry/Entity Type

Business

Contact Information for Business Card

Font styles to use
Sans Serif

Requirements
Nice to have
• As we are a veteran owned company, it would be nice to incorporate an American flag into the design. Maybe on the back?

```html
<!DOCTYPE html>
<html lang="en">
<head>
<meta charset="utf-8">
<title>Ridgeline Inc — Business Card</title>
<link href="https://fonts.googleapis.com/css2?family=Open+Sans:wght@400;600;800&display=swap" rel="stylesheet">
<style>
  :root {
    --backdrop: #8a8b8d;
    --card-white: #f5f5f5;
    --brand-green: #6dbd45;
    --accent-green: #5aaa35;
    --ink: #2b2b2b;
    --mark-dark: #2f2f2f;
    --rule: #555;
    --flag-tone: #b8a3a8;
  }
  * { margin: 0; padding: 0; box-sizing: border-box; }
  html, body { width: 1200px; height: 1200px; overflow: hidden; }
  body {
    background: var(--backdrop);
    font-family: "Open Sans", sans-serif;
    position: relative;
  }
  .card { position: absolute; }

  /* Front */
  .card-front {
    left: 212px; top: 162px; width: 782px; height: 448px;
    background: var(--card-white);
    border-left: 5px solid var(--brand-green);
    border-right: 4px solid var(--brand-green);
    border-top: 4px solid #c9c9c9;
  }
  .front-brand {
    position: absolute; left: 384px; top: 80px;
    display: flex; align-items: center; gap: 12px;
  }
  .brand-square { width: 50px; height: 50px; background: var(--mark-dark); border-radius: 6px; }
  .front-brand .brand-name {
    font-weight: 800; font-size: 34px; color: var(--brand-green); letter-spacing: 1px;
  }
  .person-name {
    position: absolute; left: 36px; top: 204px;
    font-weight: 600; font-size: 24px; color: var(--ink);
  }
  .person-title {
    position: absolute; left: 37px; top: 236px;
    font-size: 18px; color: var(--accent-green);
  }
  .divider {
    position: absolute; left: 37px; top: 264px; width: 705px; height: 1px; background: var(--rule);
  }
  .accent-bar {
    position: absolute; left: 0; top: 288px; width: 10px; height: 118px; background: var(--brand-green);
  }
  .contact-list { position: absolute; left: 44px; top: 284px; list-style: none; }
  .contact-list li {
    display: flex; align-items: center; height: 24.3px;
    font-size: 16px; color: var(--ink); word-spacing: 3px;
  }
  .contact-list svg { width: 20px; height: 20px; margin-right: 20px; flex: none; }

  /* Back */
  .card-back {
    left: 206px; top: 658px; width: 798px; height: 456px;
    background: var(--brand-green);
  }
  .flag-area {
    position: absolute; left: 102px; top: 90px; width: 92px; height: 76px;
    background: linear-gradient(160deg, #4a5a8c 0%, #c86a6a 55%, #e8e2e2 100%);
    border-radius: 4px;
  }
  .back-brand {
    position: absolute; left: 82px; top: 188px;
    display: flex; align-items: center; gap: 22px;
  }
  .back-brand .brand-square { width: 94px; height: 94px; border-radius: 10px; }
  .back-brand .brand-name {
    font-weight: 800; font-size: 62px; color: #fff; letter-spacing: 1px;
  }
</style>
</head>
<body>

<section class="card card-front" aria-label="Business card front">
  <div class="front-brand">
    <div class="brand-square"></div>
    <span class="brand-name">RIDGELINE INC</span>
  </div>
  <h1 class="person-name">MARCUS HALE</h1>
  <p class="person-title">Founder &amp; CEO</p>
  <div class="divider"></div>
  <div class="accent-bar"></div>
  <ul class="contact-list">
    <li>
      <svg viewBox="0 0 20 20"><rect x="5" y="1.5" width="10" height="17" rx="2" fill="none" stroke="#5aaa35" stroke-width="1.5"/><circle cx="10" cy="15.5" r="1" fill="#5aaa35"/></svg>
      1 (800) 555-0147 (2210)
    </li>
    <li>
      <svg viewBox="0 0 20 20"><path d="M2 8c0-3 16-3 16 0v2h-4V8H6v2H2z" fill="#5aaa35"/><path d="M5 11h10l2 7H3z" fill="#5aaa35"/><circle cx="10" cy="14" r="2" fill="#f5f5f5"/></svg>
      1 (400) 555-0192
    </li>
    <li>
      <svg viewBox="0 0 20 20"><rect x="5" y="2" width="10" height="5" fill="#5aaa35"/><rect x="2" y="7" width="16" height="7" rx="1.5" fill="#5aaa35"/><rect x="5" y="12" width="10" height="6" fill="#5aaa35" stroke="#f5f5f5" stroke-width="1"/></svg>
      1 (000) 555-0163
    </li>
    <li>
      <svg viewBox="0 0 20 20"><rect x="2" y="4" width="16" height="12" fill="none" stroke="#5aaa35" stroke-width="1.3"/><path d="M2 4l8 7 8-7M2 16l6-6M18 16l-6-6" fill="none" stroke="#5aaa35" stroke-width="1.3"/></svg>
      info@ridgelineworks.com
    </li>
    <li>
      <svg viewBox="0 0 20 20"><circle cx="10" cy="10" r="8" fill="none" stroke="#5aaa35" stroke-width="1.3"/><ellipse cx="10" cy="10" rx="3.5" ry="8" fill="none" stroke="#5aaa35" stroke-width="1.1"/><path d="M2 10h16M3.5 6h13M3.5 14h13" stroke="#5aaa35" stroke-width="1.1"/></svg>
      www.ridgelineworks.com
    </li>
  </ul>
</section>

<section class="card card-back" aria-label="Business card back">
  <div class="flag-area" role="img" aria-label="American flag waving on a pole"></div>
  <div class="back-brand">
    <div class="brand-square"></div>
    <span class="brand-name">RIDGELINE INC</span>
  </div>
</section>

</body>
</html>
```